Flyer-Gestaltung für Pelz- & Gold-Ankauf
Zielgruppe
Pelz & Gold Ankauf Wendtner in Ottobrunn
Unsere Zielgruppe sind Rentner und Senioren
Wir kaufen Pelze Gold und Bernstein auf
Aber Hauptsächlich geht es um den Pelzankauf
Daher suchen wir ein hochwertiges Design was direkt ins Auge fällt
Aufgabenstellung
Wir brauchen ein vertrauenswürdiges und gleich auffälliges Inserat mit sehr hochwertigen Bildern und kleinen seriösen Texten.
Der größte Teil der Werbung sollte für die Pelze sein und ein kleiner für Bernstein und Goldschmuck.
Folgende Vorgaben müssen berücksichtigt werden:
- 231mm breite und 324mm Höhe
- Hochformat in der Zeitung
Für den Text sind folgende Informationen zu integrieren:
Wichtig wäre das unsere Pelz Aktion gilt nur 4 - 6 Tage
Wir zahlen bis zu 10 000 für Pelze
Unser Ankauf ist in ganz Ottobrunn, Unterhaching, Feldmoching, Aying Brunthal, Germering, Garching und Umgebung
Information zu den Anhängen:
Das 1 Bild war unsere alte Anzeige von damals aber die nicht grade besonders ist
Das 2 Bild und 3 Bild wäre die Konkurrenz
Es sollte selbstverständlich in jedem Punkt besser ausschauen
Wir möchten nicht der Konkurrenz ähneln
Bild 4 wäre ein Design wo uns gut gefällt von einen Bernstein Ankauf
Es sollte direkt ins Auge fallen
Ich hoffe auf ein auffälliges besonderes Design das die Leute überzeugt lieber bei mir ihren Pelz zu verkaufen

```html
<!DOCTYPE html>
<html lang="de">
<head>
<meta charset="utf-8">
<title>Pelz- & Goldankauf Wendtner – Pelz zu Bargeld</title>
<link rel="stylesheet" href="https://fonts.googleapis.com/css2?family=Montserrat:wght@700;800&family=Nunito+Sans:ital,wght@0,400;0,600;0,700;1,400&display=swap">
<style>
  :root {
    --bg-dark: #22211d;
    --bg-glow: #8d8272;
    --gold-light: #efdc9c;
    --gold-mid: #d2b56a;
    --gold-deep: #b8963f;
    --gold-text: #dcc585;
    --ink: #1e1d1a;
    --white: #ffffff;
    --fur-light: #c98a55;
    --fur-dark: #7a4526;
  }
  * { margin: 0; padding: 0; box-sizing: border-box; }
  html, body { width: 855px; height: 1200px; overflow: hidden; background: var(--bg-dark); }
  .flyer {
    position: relative; width: 855px; height: 1200px; overflow: hidden;
    background: radial-gradient(circle at 420px 265px, var(--bg-glow) 0, #4a463e 150px, var(--bg-dark) 360px);
    font-family: "Nunito Sans", Arial, sans-serif; color: var(--white);
  }
  .abs { position: absolute; line-height: 1; white-space: nowrap; }

  .top-banner {
    position: absolute; left: 169px; top: 0; width: 515px; height: 71px;
    background: linear-gradient(90deg, var(--gold-light), var(--gold-mid) 60%, var(--gold-deep));
    border: 1px solid #f4e6b5; border-top: none;
    display: flex; align-items: center; justify-content: center;
    color: var(--ink); font-size: 34px;
  }
  .top-banner strong { font-weight: 700; margin-left: 9px; letter-spacing: .5px; }

  .coat-photo {
    position: absolute; left: 28px; top: 113px; width: 444px; height: 650px;
    border-radius: 42% 42% 12% 12% / 14% 14% 8% 8%;
    background: radial-gradient(ellipse at 50% 40%, var(--fur-light), #a8673a 55%, var(--fur-dark) 100%);
  }

  .intro { right: 65px; top: 125px; font-size: 32px; }
  .pelz { right: 72px; top: 172px; font-family: Montserrat, Arial, sans-serif; font-weight: 800; font-size: 70px; }
  .pelz small { font-family: "Nunito Sans", Arial, sans-serif; font-weight: 400; font-size: 33px; margin-left: 10px; }
  .bargeld { right: 63px; top: 237px; font-family: Montserrat, Arial, sans-serif; font-weight: 800; font-size: 75px; }

  .offer-rule { position: absolute; left: 481px; top: 329px; width: 2px; height: 396px; background: var(--gold-mid); }
  .offer-lead { left: 500px; top: 344px; font-size: 25px; }
  .offer-amount { left: 500px; top: 378px; color: var(--gold-mid); font-family: Montserrat, Arial, sans-serif; font-weight: 800; font-size: 60px; }
  .offer-amount span { font-size: 37px; font-weight: 700; }
  .offer-scope { left: 500px; top: 442px; font-size: 24px; }
  .footnote { left: 500px; font-size: 13px; font-style: italic; color: #e6e2d8; }
  .footnote.one { top: 485px; }
  .footnote.two { top: 505px; }
  .reason { left: 500px; font-size: 21px; }
  .reason.one { top: 553px; }
  .reason.two { top: 585px; }
  .action-title { left: 500px; top: 624px; font-family: Montserrat, Arial, sans-serif; font-weight: 700; font-size: 32px; letter-spacing: -.5px; }
  .action-dates { left: 500px; top: 673px; font-family: Montserrat, Arial, sans-serif; font-weight: 700; font-size: 34px; color: var(--gold-text); }

  .fur-types { left: 0; width: 855px; top: 771px; text-align: center; font-size: 23.5px; }

  .gold-band {
    position: absolute; left: 0; top: 856px; width: 855px; height: 160px;
    background: linear-gradient(90deg, #d9c27a, var(--gold-light) 45%, var(--gold-mid) 80%, var(--gold-deep));
    border-top: 2px solid #c9c6bf; border-bottom: 2px solid #c9c6bf;
  }
  .band-lead { left: 71px; top: 882px; font-size: 23px; color: var(--ink); }
  .band-title { left: 71px; top: 920px; font-family: Montserrat, Arial, sans-serif; font-weight: 700; font-size: 35px; line-height: 38px; color: var(--ink); white-space: normal; width: 360px; }

  .jewel-photo {
    position: absolute; top: 824px; width: 178px; height: 220px;
    border-radius: 45% 45% 30% 30% / 22% 22% 18% 18%;
  }
  .jewel-photo.amber { left: 433px; background: radial-gradient(ellipse at 50% 55%, #e07a1c 0, #2b2b2f 45%, #121214 100%); }
  .jewel-photo.gold { left: 625px; background: radial-gradient(ellipse at 50% 55%, #c9a54f 0, #2b2b2f 45%, #121214 100%); }

  .info-col { position: absolute; top: 1058px; height: 114px; border-left: 2px solid var(--gold-mid); padding-left: 9px; color: var(--gold-text); }
  .info-col .abs { position: absolute; left: 9px; }
  .info-col.address { left: 47px; width: 200px; }
  .info-col.hours { left: 266px; width: 250px; }
  .info-col.area { left: 531px; width: 300px; }
  .t19 { font-size: 19px; }
  .t18 { font-size: 18px; }
  .company { font-size: 29px; font-weight: 600; letter-spacing: .5px; }
  .phone { font-size: 29px; font-weight: 700; letter-spacing: 1px; }
</style>
</head>
<body>
<main class="flyer">
  <header class="top-banner">Pelz- &amp; Goldankauf <strong>WENDTNER</strong></header>

  <div class="coat-photo" role="img" aria-label="Foto: brauner Nerzmantel mit breitem Kragen und Gürtel auf einer Schneiderpuppe"></div>

  <p class="abs intro">Machen Sie jetzt Ihren</p>
  <h1 class="abs pelz">PELZ<small>zu</small></h1>
  <p class="abs bargeld">BARGELD!</p>

  <div class="offer-rule"></div>
  <p class="abs offer-lead">Wir zahlen bis zu</p>
  <p class="abs offer-amount"><span>€</span>10.000,-</p>
  <p class="abs offer-scope">für alle Arten von Pelzen*</p>
  <p class="abs footnote one">* In Verbindung Pelz mit Gold</p>
  <p class="abs footnote two">* Ankauf auch von defekten Pelzen</p>
  <p class="abs reason one">Aufgrund der hohen</p>
  <p class="abs reason two">Nachfrage in Osteuropa,</p>
  <p class="abs action-title">5-TAGE-AKTION:</p>
  <p class="abs action-dates">10.09.-15.09.2021</p>

  <p class="abs fur-types">Füchse aller Art • Bisam • Persianer • Zobel • Chinchilla • Nerze • Nutria...</p>

  <section class="gold-band"></section>
  <p class="abs band-lead">Wir kaufen auch jede Art von</p>
  <h2 class="abs band-title">BERNSTEIN &amp; GOLDSCHMUCK</h2>
  <div class="jewel-photo amber" role="img" aria-label="Foto: Bernsteinkette auf schwarzer Schmuckbüste"></div>
  <div class="jewel-photo gold" role="img" aria-label="Foto: Goldkette auf schwarzer Schmuckbüste"></div>

  <div class="info-col address">
    <p class="abs t19" style="top:2px">Pelz- &amp; Goldankauf</p>
    <p class="abs company" style="top:30px">WENDTNER</p>
    <p class="abs t18" style="top:70px">Lindenallee 37</p>
    <p class="abs t18" style="top:96px">85521 Ottobrunn</p>
  </div>
  <div class="info-col hours">
    <p class="abs t18" style="top:3px">Montag-Samstag</p>
    <p class="abs t18" style="top:31px">nach telefonischer</p>
    <p class="abs t18" style="top:53px">Terminvereinbarung unter</p>
    <p class="abs phone" style="top:83px">089 612 480 37</p>
  </div>
  <div class="info-col area">
    <p class="abs t18" style="top:2px"><strong>ANKAUF</strong> in ganz</p>
    <p class="abs t18" style="top:24px">Kirchheim, Oberhaching,</p>
    <p class="abs t18" style="top:46px">Aubing, Brunnthal, Putzbrunn,</p>
    <p class="abs t18" style="top:69px">Neukeferloh, Deisenhofen,</p>
    <p class="abs t18" style="top:91px">Ottobrunn und Umgebung</p>
  </div>
</main>
</body>
</html>
```